Faithful Oaks Fellowship (FOF)
• The Prayer arm of GRCA which enables members to delight themselves in the purpose and work of God
• Equip members with the instrument of prayer to walk with God so that they can make lasting changes here on Earth
• Coordinate projects like the Dawn Vigil Circle, Lantern Night Vigil Series, Chain Prayers, Prayer Projects, Prayer Retreats, and the Worldwide Vigil Circle
• Manage the GRCA Prayer Academy
• Goal is transformation and dominion
• Build members to stand as mighty men giving themselves continually to prayer

You learn how to pray by praying
Join the Faithful Oaks Fellowship!

```html
<!DOCTYPE html>
<html lang="en">
<head>
<meta charset="utf-8">
<title>Faithful Oaks Fellowship – Prayer Flyer</title>
<link href="https://fonts.googleapis.com/css2?family=Great+Vibes&family=Open+Sans:wght@700&family=Didact+Gothic&family=Arimo:wght@400;700&display=swap" rel="stylesheet">
<style>
  :root {
    --brand-blue: #0d6e9e;
    --brand-blue-dark: #0a5a83;
    --link-blue: #1d7fb8;
    --ink: #1c1c1c;
    --body-ink: #2a2a2a;
    --paper: #ffffff;
    --sky-gold: #f6d77a;
    --sky-light: #fbefc4;
    --sky-blue: #8fb4c9;
    --field-green: #5f8a2e;
    --divider: #9cc3da;
  }
  * { box-sizing: border-box; margin: 0; padding: 0; }
  html, body { width: 1200px; height: 900px; overflow: hidden; background: var(--paper); }
  .flyer { position: relative; width: 1200px; height: 900px; background: var(--paper); overflow: hidden; }

  .hero-photo {
    position: absolute; left: 0; top: 0; width: 1200px; height: 470px;
    background:
      linear-gradient(180deg, rgba(143,180,201,0.0) 0%, rgba(143,180,201,0) 55%, rgba(95,138,46,0.9) 72%, var(--field-green) 100%),
      radial-gradient(ellipse at 18% 62%, #fff6d6 0%, var(--sky-gold) 22%, rgba(246,215,122,0.6) 45%, transparent 70%),
      linear-gradient(90deg, var(--sky-light) 0%, #e9d9a0 40%, var(--sky-blue) 100%);
  }
  .hero-wave { position: absolute; left: 0; top: 0; width: 1200px; height: 470px; }

  .headline { position: absolute; left: 70px; top: 95px; color: var(--ink); }
  .headline-script { font-family: "Great Vibes", cursive; line-height: 1; }
  .headline-script .small { font-size: 48px; }
  .headline-script .large { font-size: 96px; }
  .headline-sub { font-family: "Open Sans", sans-serif; font-weight: 700; font-size: 27px; margin-top: -12px; margin-left: 8px; }

  .mission-list { position: absolute; left: 44px; top: 418px; width: 610px; list-style: none;
    font-family: "Didact Gothic", sans-serif; font-size: 20px; line-height: 32px; color: var(--body-ink); }
  .mission-list li { margin-bottom: 18px; }
  .mission-list li::before { content: ""; display: inline-block; width: 7px; height: 7px; border-radius: 50%;
    background: var(--brand-blue); margin-right: 5px; vertical-align: middle; }

  .column-divider { position: absolute; left: 693px; top: 450px; width: 2px; height: 420px;
    background: linear-gradient(180deg, var(--divider), var(--brand-blue) 40%, rgba(13,110,158,0.15)); }

  .invite { position: absolute; left: 745px; top: 470px; width: 420px; text-align: center; }
  .invite-script { font-family: "Great Vibes", cursive; font-size: 36px; color: var(--brand-blue); line-height: 1.1; }
  .invite-call { font-family: "Arimo", sans-serif; font-weight: 700; font-size: 22px; color: var(--ink); margin-top: 4px; }

  .name-plate { position: absolute; left: 795px; top: 560px; width: 312px; height: 114px;
    border: 4px solid var(--brand-blue); border-radius: 14px; background: var(--paper);
    display: flex; align-items: center; justify-content: center; gap: 14px; }
  .name-plate .dot { width: 22px; height: 22px; border-radius: 50%; background: var(--brand-blue); flex: none; }
  .name-plate .name { font-family: "Didact Gothic", sans-serif; font-size: 24px; color: var(--brand-blue); line-height: 1.2; }

  .contact { position: absolute; left: 745px; top: 704px; font-family: "Arimo", sans-serif; color: var(--ink); }
  .contact-title { font-weight: 700; font-size: 19px; letter-spacing: 0.2px; margin-bottom: 10px; }
  .contact-line { font-size: 15px; line-height: 31px; color: var(--link-blue); }
  .contact-line b { color: var(--ink); }
  .contact-line .sep { color: var(--ink); margin: 0 10px; }
</style>
</head>
<body>
<main class="flyer">
  <div class="hero-photo" role="img" aria-label="Photo of a man with raised arms standing in a sunlit green meadow at sunrise"></div>

  <svg class="hero-wave" viewBox="0 0 1200 470" aria-hidden="true">
    <path d="M0,330 C250,260 500,330 760,395 C950,440 1100,420 1200,375 L1200,470 L0,470 Z" fill="var(--brand-blue)"/>
    <path d="M0,318 C250,250 500,318 760,383" fill="none" stroke="#ffffff" stroke-width="3" opacity="0.8"/>
    <path d="M0,415 C250,355 460,390 700,425 C900,452 1060,440 1200,415 L1200,470 L0,470 Z" fill="var(--paper)"/>
  </svg>

  <div class="headline">
    <div class="headline-script"><span class="small">to</span> <span class="large">worship</span></div>
    <div class="headline-sub">Him in Spirit and in Truth</div>
  </div>

  <ul class="mission-list">
    <li>The Prayer arm of GRCA which enables members to delight themselves in the purpose &amp; work of God.</li>
    <li>Equip members with the instrument of prayer to walk with God so that they can make lasting changes here on Earth.</li>
    <li>Coordinate projects like the Dawn Vigil Circle, Lantern Night Vigil Series, Chain Prayers, Prayer Projects, Prayer Retreats &amp; the Worldwide Vigil Circle.</li>
    <li>Manage the GRCA Prayer Academy.</li>
    <li>Goal is transformation and dominion</li>
    <li>Build members to stand as mighty men giving themselves continually to prayer</li>
  </ul>

  <div class="column-divider"></div>

  <div class="invite">
    <p class="invite-script">Learn how to pray by praying</p>
    <p class="invite-call">Join the Faithful Oaks Fellowship!</p>
  </div>

  <div class="name-plate">
    <span class="dot"></span>
    <span class="name">Grace Covenant<br>Assembly</span>
  </div>

  <address class="contact" style="font-style:normal">
    <p class="contact-title">GRACE COVENANT ASSEMBLY</p>
    <p class="contact-line"><b>Address:</b> Riverside / Eastport:</p>
    <p class="contact-line">No. 48 Harbor Lane, Riverside, Coastal State.</p>
    <p class="contact-line"><b>Phone:</b> +234 801 555 0192, +234 802 555 0147</p>
    <p class="contact-line"><b>Email:</b> info@gracecovenant.org<span class="sep">|</span>admin@gracecovenant.org</p>
  </address>
</main>
</body>
</html>
```